CD cover for rock-nproll song

I need a logo design for a CD cover for a soon-to-be released rock song by my band, VEXO.
The song is called "Darlin Don't Stay". The logo should include the band logo as well as some representation of the song title. The song is about the end of a romantic relationship.

on -line music consumers

Baby

• VEXO logo (provided)
• Name of song- "Darlin Don't Stay"
• A design that reflects the meaning in the song... "Darlin Don't Stay, it's time to go, it's all over. What you said to me, made me see we've got nothing". That is the chorus- the song is about a relationship coming apart.

```html
<!DOCTYPE html>
<html lang="en">
<head>
<meta charset="utf-8">
<title>Darlin Don't Stay — VEXO</title>
<link href="https://fonts.googleapis.com/css2?family=Bebas+Neue&display=swap" rel="stylesheet">
<style>
  :root {
    --ink: #000000;
    --paper: #f4f4f4;
    --bokeh: #d6d6d6;
    --tone-light: #b4b4b4;
    --tone-mid: #7a7a7a;
    --tone-dark: #262626;
    --figure-dark: #1c1c1c;
    --hat-grey: #8e8e8e;
    --skin-light: #a8a8a8;
    --hair-light: #c4c4c4;
  }
  html, body {
    margin: 0;
    padding: 0;
    width: 1200px;
    height: 1154px;
    overflow: hidden;
    background: var(--ink);
  }
  .cover {
    position: relative;
    width: 1200px;
    height: 1154px;
    overflow: hidden;
  }
  .cover__photo {
    position: absolute;
    inset: 0;
    background:
      radial-gradient(ellipse 170px 210px at 1060px 370px, var(--hat-grey) 0%, rgba(142,142,142,0.85) 55%, rgba(142,142,142,0) 100%),
      radial-gradient(ellipse 150px 200px at 1060px 720px, var(--skin-light) 0%, rgba(168,168,168,0.8) 55%, rgba(168,168,168,0) 100%),
      radial-gradient(ellipse 240px 260px at 1000px 1030px, var(--hair-light) 0%, rgba(196,196,196,0.7) 50%, rgba(196,196,196,0) 100%),
      radial-gradient(ellipse 270px 250px at 660px 150px, var(--figure-dark) 0%, rgba(28,28,28,0.9) 55%, rgba(28,28,28,0) 100%),
      radial-gradient(ellipse 170px 200px at 600px 330px, #5a5a5a 0%, rgba(90,90,90,0.7) 55%, rgba(90,90,90,0) 100%),
      radial-gradient(ellipse 300px 560px at 720px 820px, var(--figure-dark) 0%, rgba(30,30,30,0.85) 55%, rgba(30,30,30,0) 100%),
      radial-gradient(ellipse 300px 320px at 200px 220px, var(--bokeh) 0%, rgba(200,200,200,0.5) 55%, rgba(200,200,200,0) 100%),
      radial-gradient(ellipse 260px 300px at 160px 760px, #8a8a8a 0%, rgba(120,120,120,0.4) 60%, rgba(120,120,120,0) 100%),
      linear-gradient(90deg, var(--tone-light) 0%, var(--tone-mid) 35%, var(--tone-dark) 55%, #4a4a4a 80%, var(--tone-mid) 100%);
  }
  .cover__bars {
    position: absolute;
    inset: 0;
    width: 1200px;
    height: 1154px;
  }
  .cover__bars polygon { fill: var(--ink); }
  .cover__title {
    position: absolute;
    left: 0;
    width: 1194px;
    top: 548px;
    margin: 0;
    text-align: center;
    font-family: "Bebas Neue", "Oswald", sans-serif;
    font-weight: 400;
    font-size: 82px;
    line-height: 1;
    letter-spacing: 1px;
    color: var(--paper);
    white-space: nowrap;
  }
  .cover__band {
    position: absolute;
    left: 0;
    width: 1194px;
    top: 634px;
    margin: 0;
    text-align: center;
    font-family: "Bebas Neue", "Oswald", sans-serif;
    font-weight: 400;
    font-size: 36px;
    line-height: 1;
    letter-spacing: 2px;
    color: var(--paper);
  }
</style>
</head>
<body>
  <main class="cover">
    <div class="cover__photo" role="img" aria-label="Black-and-white photograph of a couple in winter hats and coats, heads bowed and turned away from each other, against a soft blurred wooded background"></div>
    <svg class="cover__bars" viewBox="0 0 1200 1154" aria-hidden="true">
      <polygon points="420,226 622,164 652,264 450,327"/>
      <polygon points="905,529 1200,546 1200,656 890,640"/>
    </svg>
    <h1 class="cover__title">Darlin Don't Stay</h1>
    <p class="cover__band">VEXO</p>
  </main>
</body>
</html>
```